Simple Print Ad for Nonprofit Crisis Call Line

Nonprofit agency needs a simple ad FOR PRINT PUBLICATIONS (newspapers, magazines, etc.) to advertise its Crisis Call Line. Ad should be GRAPHICALLY SIMPLE and bold, eye-catching, and easily increased/decreased in size. The graphic format needs to be at least 300 DPI and should be in both a jpeg and pdf. We will need color and black and white versions.

SIZE OF AD: Since the ad will appear in multiple publications, the ads need to be scalable, or easily increased/decreased in size to increase the chances that publications will place them and to avoid having to have dozens of individually designed ads.

For the purpose of the initial ad design, please design a horizontal ad that is close to 4" tall and 5" long and a vertical ad that is 21/2" wide by 41/2" long. The winning artist will need to provide us will all the ad elements as separate files so that they can be manipulated to produce different size ads. The artist may also be asked to make additional ads in different sizes and languages in the future.
Updates

Thank you to everyone that has submitted a design. We are in the process of reviewing the designs and compiling our comments and questions. Please give us a few days to respond.

Industry/Entity Type

Call

Requirements
Must have
• Agency logo and the text included.
Should not have
• Any other text other than what is provided.

```html
<!DOCTYPE html>
<html lang="en">
<head>
<meta charset="utf-8">
<title>The Crisis Line – Harbor &amp; Hearth Services</title>
<link rel="stylesheet" href="https://fonts.googleapis.com/css2?family=Noto+Serif:ital,wght@0,300;0,400;0,700;1,700&display=swap">
<style>
  :root {
    --leaf-green: #84c126;
    --brand-green: #3aa535;
    --frame-grey: #6f6f6f;
    --tag-grey: #858585;
    --ink: #1a1a1a;
    --paper: #ffffff;
    --shadow: #e4e4e4;
  }
  html, body {
    margin: 0;
    padding: 0;
    width: 1200px;
    height: 1000px;
    overflow: hidden;
    background: var(--paper);
  }
  .canvas {
    position: relative;
    width: 1200px;
    height: 1000px;
    font-family: "Noto Serif", Georgia, serif;
  }
  .ad-shapes {
    position: absolute;
    left: 0;
    top: 0;
  }
  .headline {
    position: absolute;
    margin: 0;
    line-height: 1;
    font-size: 50px;
    letter-spacing: -0.5px;
    white-space: nowrap;
  }
  .headline-person { left: 398px; top: 302px; font-weight: 300; color: var(--paper); font-size: 48px; }
  .headline-problem { left: 342px; top: 352px; font-weight: 700; color: var(--paper); }
  .headline-time { left: 457px; top: 396px; font-weight: 700; color: var(--ink); }

  .crisis-contact {
    position: absolute;
    left: 343px;
    top: 612px;
    width: 195px;
  }
  .crisis-name {
    margin: 0;
    font-size: 25px;
    font-weight: 700;
    color: var(--brand-green);
    line-height: 1.1;
    white-space: nowrap;
  }
  .crisis-phone {
    margin: 0;
    font-size: 27px;
    font-weight: 300;
    color: var(--ink);
    line-height: 1.15;
    letter-spacing: 0.5px;
    white-space: nowrap;
  }
  .crisis-tag {
    margin: 4px 0 0;
    background: var(--tag-grey);
    color: var(--paper);
    font-size: 14.5px;
    font-style: italic;
    font-weight: 700;
    height: 20px;
    line-height: 20px;
    padding-left: 20px;
    white-space: nowrap;
  }

  .agency-name {
    position: absolute;
    left: 680px;
    top: 616px;
    width: 206px;
    margin: 0;
    text-align: center;
    font-size: 25px;
    font-weight: 400;
    line-height: 1.1;
    color: var(--brand-green);
  }
</style>
</head>
<body>
<main class="canvas">
  <svg class="ad-shapes" width="1200" height="1000" viewBox="0 0 1200 1000" aria-hidden="true">
    <defs>
      <linearGradient id="bubble-shadow" x1="0" y1="0" x2="1" y2="1">
        <stop offset="0" stop-color="#f6f6f6"/>
        <stop offset="1" stop-color="#dcdcdc"/>
      </linearGradient>
    </defs>
    <!-- card frame -->
    <path class="frame-grey" d="M296 744 H904 Q910 744 910 738 V258" fill="none" stroke="var(--frame-grey)" stroke-width="6"/>
    <path class="frame-green" d="M291 741 V257 Q291 251 297 251 H908" fill="none" stroke="var(--leaf-green)" stroke-width="6"/>
    <!-- speech bubble shadow -->
    <path d="M300 260 H780 C790 400 725 480 625 517 L551 622 L584 532 C470 565 352 535 300 450 Z" fill="url(#bubble-shadow)"/>
    <!-- speech bubble -->
    <path d="M300 260 H757 C765 400 700 472 612 507 L551 622 L570 522 C460 553 350 522 300 437 Z" fill="var(--leaf-green)"/>
    <!-- agency mark placeholder -->
    <circle cx="783" cy="556" r="36" fill="var(--brand-green)"/>
  </svg>

  <p class="headline headline-person">Any person</p>
  <p class="headline headline-problem">any problem</p>
  <p class="headline headline-time">any time</p>

  <div class="crisis-contact">
    <p class="crisis-name">The Crisis Line</p>
    <p class="crisis-phone">555-019-2834</p>
    <p class="crisis-tag">Free and confidential</p>
  </div>

  <p class="agency-name">Harbor &amp;<br>Hearth Services</p>
</main>
</body>
</html>
```